IT Recruitment Brochure

5 page brochure to promote our company's entrance into the Recruitment field
Target Market(s)
IT Professionals
Industry/Entity Type
It Company
Requirements
Must have
- 5 pages
norvalent silver partner logo
pelridy partner logo
quolix partner logo
oslpa partner logo

```html
<!DOCTYPE html>
<html lang="en">
<head>
<meta charset="utf-8">
<title>Nexora IT – Our Process</title>
<link href="https://fonts.googleapis.com/css2?family=Roboto:wght@700;900&family=Roboto+Condensed:wght@700&family=Playfair+Display:wght@700&display=swap" rel="stylesheet">
<style>
  :root {
    --page-bg: #f1f1f1;
    --band-top: #4cff00;
    --band-bottom: #aaff00;
    --side-tab: #000000;
    --text-light: #ffffff;
    --text-dark: #000000;
    --circle-core: #6cff3a;
    --circle-edge: #1fd400;
  }
  * { margin: 0; padding: 0; box-sizing: border-box; }
  html, body {
    width: 1200px; height: 900px; overflow: hidden;
    background: var(--page-bg);
  }
  .page {
    position: absolute; left: 0; top: 25px;
    width: 1200px; height: 848px;
    box-shadow: 0 0 14px rgba(0,0,0,0.18);
  }
  .intro-band {
    position: absolute; left: 0; top: 0;
    width: 1200px; height: 424px;
    background: var(--band-top);
  }
  .intro-text {
    position: absolute; left: 273px; top: 67px; width: 656px;
    font-family: "Roboto", Arial, sans-serif;
    font-weight: 700; font-size: 20px; line-height: 29.4px;
    color: var(--text-light);
  }
  .intro-line {
    display: block; white-space: nowrap;
    text-align: justify; text-align-last: justify;
  }
  .intro-line.is-last { text-align: left; text-align-last: left; }
  .process-band {
    position: absolute; left: 0; top: 424px;
    width: 1200px; height: 424px;
    background: var(--band-bottom);
  }
  .side-tab {
    position: absolute; left: 0; top: 0;
    width: 73px; height: 424px;
    background: var(--side-tab);
  }
  .side-tab-label {
    position: absolute; left: 37px; top: 219px;
    transform: translate(-50%, -50%) rotate(-90deg);
    white-space: nowrap;
    font-family: "Playfair Display", Georgia, serif;
    font-weight: 700; font-size: 25px;
    color: var(--text-light);
  }
  .process-diagram {
    position: absolute; left: 0; top: 0;
  }
  .circle-label {
    font-family: "Roboto", Arial, sans-serif;
    font-weight: 900; font-size: 19px;
    fill: var(--text-light);
  }
  .core-label {
    font-family: "Roboto Condensed", Arial, sans-serif;
    font-weight: 700; font-size: 23px;
    fill: var(--text-dark);
  }
</style>
</head>
<body>
  <div class="page">
    <section class="intro-band">
      <p class="intro-text">
        <span class="intro-line">Nexora IT recruitment is changing the way recruitment is</span>
        <span class="intro-line">practiced. Nexora IT works hand in hand with training and</span>
        <span class="intro-line">recruitment, enabling us to identify the gap in the Australian</span>
        <span class="intro-line">I.T. industry and bridging that gap by providing the most re-</span>
        <span class="intro-line">cent and in demand certifications to our candidates. Working</span>
        <span class="intro-line">with employers, we know what their demand is, allowing us</span>
        <span class="intro-line">to headhunt job seekers suited best for the respective roles,</span>
        <span class="intro-line">while also delivering them with essential on job skills such as</span>
        <span class="intro-line">communication and interpersonal skills through our Work-</span>
        <span class="intro-line is-last">FitTM program.</span>
      </p>
    </section>

    <section class="process-band">
      <div class="side-tab"><h2 class="side-tab-label">Our Process</h2></div>

      <svg class="process-diagram" width="1200" height="424" viewBox="0 449 1200 424" aria-label="Process diagram: workFit, Training and Certification around Recruitment">
        <defs>
          <radialGradient id="circleFill" cx="50%" cy="45%" r="55%">
            <stop offset="0%" stop-color="var(--circle-core)"/>
            <stop offset="100%" stop-color="var(--circle-edge)"/>
          </radialGradient>
          <linearGradient id="coreFill" x1="0" y1="0" x2="0" y2="1">
            <stop offset="0%" stop-color="#b8ff8a"/>
            <stop offset="60%" stop-color="#f0ffe8"/>
            <stop offset="100%" stop-color="#ffffff"/>
          </linearGradient>
        </defs>

        <g class="process-step" stroke="#ffffff" stroke-width="8" fill="url(#circleFill)">
          <circle cx="600" cy="583" r="94"/>
          <circle cx="500" cy="740" r="86"/>
          <circle cx="697" cy="740" r="86"/>
        </g>

        <polygon class="process-core" points="505,633 695,633 600,797"
                 fill="url(#coreFill)" stroke="#ffffff" stroke-width="8" stroke-linejoin="round"/>

        <text class="circle-label" x="600" y="581" text-anchor="middle">workFit</text>
        <text class="circle-label" x="495" y="758" text-anchor="middle">Training</text>
        <text class="circle-label" x="706" y="759" text-anchor="middle">Certification</text>

        <text class="core-label" x="600" y="674" text-anchor="middle">Recruitment</text>
        <text class="core-label" x="600" y="706" text-anchor="middle">@ NXI</text>
      </svg>
    </section>
  </div>
</body>
</html>
```